Executive Business Card for Healthcare Company [Need Today]

I need a business card design for a healthcare company. The only branding the company has thus far is a logo. The cards will be utilized by company executives. The design I envision will be vibrant and appealing but with a corporate feel. They shouldn't be too casual or playful. I would like to complete this project TODAY if possible.

Target Market(s)

Healthcare vendors, other executives in healthcare and pharmaceuticals

Industry/Entity Type

Pharmaceutical

Contact Information for Business Card

See attachment

Font styles to use
Serif
Sans Serif

Colors

Designer to choose colors to be used in the design.

```html
<!DOCTYPE html>
<html lang="en">
<head>
<meta charset="utf-8">
<title>Corvena Therapeutics – Business Card</title>
<link rel="stylesheet" href="https://fonts.googleapis.com/css2?family=Arimo:wght@400;700&display=swap">
<style>
  :root {
    --backdrop: #2e2e2e;
    --card: #ffffff;
    --teal: #2fb1ba;
    --mint: #5cb890;
    --ink: #5a5a5a;
    --rule: #c9c9c9;
  }
  * { margin: 0; padding: 0; box-sizing: border-box; }
  html, body { width: 1200px; height: 900px; overflow: hidden; }
  body {
    background: var(--backdrop);
    font-family: "Arimo", Arial, sans-serif;
    display: flex;
    flex-direction: column;
    align-items: center;
    justify-content: center;
    gap: 48px;
  }
  .card {
    position: relative;
    width: 660px;
    height: 377px;
    background: var(--card);
    box-shadow: 0 6px 18px rgba(0,0,0,0.45);
  }
  .card-front {
    display: flex;
    align-items: center;
    justify-content: center;
    gap: 20px;
  }
  .brand-ring { display: block; }
  .brand-name {
    color: var(--teal);
    font-weight: 400;
    font-size: 30px;
    letter-spacing: 0.5px;
  }
  .card-back .brand {
    position: absolute;
    left: 58px;
    top: 62px;
    display: flex;
    align-items: center;
    gap: 18px;
  }
  .card-back .brand-name { font-size: 28px; }
  .holder {
    position: absolute;
    left: 80px;
    top: 222px;
    font-size: 17px;
    line-height: 1.25;
    color: var(--ink);
  }
  .holder-name { color: var(--teal); font-weight: 700; }
  .email {
    position: absolute;
    left: 80px;
    top: 300px;
    font-size: 17px;
    color: var(--teal);
  }
  .contact {
    position: absolute;
    left: 440px;
    top: 152px;
    font-size: 15px;
    line-height: 1.3;
    color: var(--ink);
  }
  .contact .label { color: var(--teal); display: inline-block; width: 14px; }
  .address { margin-top: 12px; }
</style>
</head>
<body>
  <section class="card card-front">
    <svg class="brand-ring" width="104" height="104" viewBox="0 0 104 104" aria-hidden="true">
      <circle cx="52" cy="52" r="49" fill="none" stroke="var(--mint)" stroke-width="4"/>
    </svg>
    <span class="brand-name">Corvena Therapeutics</span>
  </section>

  <section class="card card-back">
    <div class="brand">
      <svg class="brand-ring" width="96" height="96" viewBox="0 0 96 96" aria-hidden="true">
        <circle cx="48" cy="48" r="45" fill="none" stroke="var(--mint)" stroke-width="4"/>
      </svg>
      <span class="brand-name">Corvena Therapeutics</span>
    </div>

    <div class="holder">
      <div class="holder-name">Daniel Mercer</div>
      <div class="holder-title">Senior Director of Marketing</div>
    </div>

    <div class="email">dmercer@corvenarx.com</div>

    <div class="contact">
      <div><span class="label">O</span> 555 214 7730</div>
      <div><span class="label">M</span> 555 382 6145</div>
      <div class="address">
        Corvena Therapeutics, LLC<br>
        118 W Larkin Avenue<br>
        Fairhaven, GA 30000
      </div>
    </div>
  </section>
</body>
</html>
```